Wordpress design for my private practice website - Psychotherapist

I would like a simple, clean, and elegant design for my private practice website. I work with both adults and children so I'd like it to appeal to both. However, since parents make the choice as to where to send their child for therapy, I want it to appeal to adults more. I would like the pictures on the site to have a calming effect - maybe using sand and water and rocks. I am attaching files with my company logo. I would also like my name incorporated into the header - Colette Brannigan, LCSW, Registered Play Therapist. I've also uploaded a picture of myself for my About Page.

I like the design of these 2 website and want something similar:
www.drlorapenwick.example
www.harwood-tallis.example

I would like a home page that highlights a calming graphic across the entire top of the page as well as my practice logo and my name.

I'd like a link to social media sites on the top of the homepage - facebook, pinterest.

I want a simple bar across the top with the following tabs:
Home
About Me (subtabs Who I Am, Specialties and Approach)
Counseling Services (subtabs Individual Counseling, Play Therapy, Sandplay Therapy,)
Fees
FAQs
Contact Me (would love this to be a fill in the blank contact form that sends info to my email address - should include name, phone number, email and a comment box for more information requested)
Blog (this will link with another wordpress blog)

Target Market(s)

Parents of children under age 12 with behavioral problems or are dealing with the breakup of their family through divorce - looking for someone to work with their young child. I also work with Adults that are overwhelmed and worried - often women that have many life stressors and are feeling burnt out on life and meeting everyone's needs. Families going through some type of trauma, including divorce or grief work. I also work with individuals going through a transition of religious beliefs - often exiting the religion of their youth and undergoing a crisis of faith at midlife.

Industry/Entity Type

Mental Health

Contact Information for Business Card

Colette Brannigan, LCSW
Registered Play Therapist
4917 Wexmoor Lane
Idaho Falls, Idaho 83404
(208)555-0187
www.stillbrookcounseling.example

On the opposite side, I'd like an appointment reminder area - with the following text:

Your next appointment is
_____/______/______ at ______am/pm
Please give 24 hrs notice if you need to cancel your appointment.

Coding

Coded - Design and coding required

Number of Pages Required

5+ page

Font styles to use
Sans Serif

Colors
33a6d7
9bcb3c
0355a3

Requirements
Must have
• I'd like it to be a wordpress site. I'm such a newby at web design - but I need to be able to add content and manage the site myself once it is up and running.
Nice to have
• I like the design of these 2 websites and want something similar:
• www.drlorapenwick.example
• www.harwood-tallis.example
• They are clean, easy to navigate and calming.
Should not have
• Should not look like a childcare website.

```html
<!DOCTYPE html>
<html lang="en">
<head>
<meta charset="utf-8">
<title>Colette Brannigan – Stillbrook Counseling</title>
<link href="https://fonts.googleapis.com/css2?family=Alike&family=Great+Vibes&family=Josefin+Sans:wght@300;400&family=Roboto:wght@400;500&family=Roboto+Condensed:wght@700&family=Montserrat:wght@400;500&display=swap" rel="stylesheet">
<style>
  :root {
    --page: #f5f5f5;
    --white: #ffffff;
    --ink: #2b2b2b;
    --muted: #555555;
    --navy: #1f5485;
    --sky: #35a9dc;
    --lime: #c4f21e;
    --lime-soft: #b8ec5e;
    --olive: #738f22;
    --olive-dark: #2e3b12;
    --olive-link: #d2e67a;
    --submit: #b7d46a;
    --social-blue: #2b5c9c;
    --social-sky: #3b8fd0;
    --social-red: #c8353a;
  }
  * { box-sizing: border-box; margin: 0; padding: 0; }
  html, body { width: 884px; height: 1200px; overflow: hidden; background: var(--page); }
  .canvas { position: relative; width: 884px; height: 1200px; overflow: hidden; background: var(--page); font-family: "Alike", serif; color: var(--ink); }
  .abs { position: absolute; }

  .topbar { left: 0; top: 0; width: 884px; height: 91px; background: var(--page); }
  .top-social { top: 29px; width: 32px; height: 32px; border-radius: 50%; }
  .top-social.one { left: 739px; background: var(--social-blue); }
  .top-social.two { left: 781px; background: var(--social-red); }

  .hero { left: 0; top: 91px; width: 884px; height: 258px;
    background: radial-gradient(ellipse at 50% 35%, #a9b9dc 0%, #5a74b4 35%, #2a3f7a 70%, #1a2a55 100%); }
  .hero-shade { left: 0; top: 91px; width: 884px; height: 258px;
    background: linear-gradient(180deg, rgba(20,30,70,0.15) 0%, rgba(20,30,70,0) 40%, rgba(10,20,50,0.45) 100%); }
  .logo-disc { left: 314px; top: 0; width: 240px; height: 162px; overflow: visible; }
  .brand-dot { left: 418px; top: 30px; width: 32px; height: 32px; border-radius: 50%; background: var(--navy); }
  .brand { left: 318px; top: 88px; width: 232px; text-align: center; font-family: "Montserrat", sans-serif; }
  .brand-name { font-size: 15px; letter-spacing: 4px; color: #555; font-weight: 400; line-height: 18px; padding-left: 4px; }
  .brand-sub { font-size: 8px; letter-spacing: 3px; color: #555; margin-top: 5px; font-weight: 500; padding-left: 3px; }
  .hero-name { left: 0; top: 192px; width: 884px; text-align: center; font-family: "Great Vibes", cursive; font-size: 68px; color: var(--lime); line-height: 1; }
  .hero-title { left: 0; top: 281px; width: 884px; text-align: center; font-family: "Roboto Condensed", sans-serif; font-weight: 700; font-size: 23px; color: var(--white); letter-spacing: 0.3px; }

  .nav { left: 0; top: 349px; width: 884px; height: 38px; background: var(--navy); }
  .nav-item { top: 359px; font-size: 13px; color: var(--white); }

  .welcome-title { left: 61px; top: 421px; font-family: "Josefin Sans", sans-serif; font-weight: 300; font-size: 30px; color: var(--ink); }
  .welcome-rule { left: 61px; top: 463px; width: 534px; height: 1px; background: #8a8a8a; }
  .welcome-copy { left: 64px; top: 481px; width: 530px; font-size: 9.6px; line-height: 13.2px; letter-spacing: -0.1px; color: #333; }
  .welcome-copy p { margin-bottom: 13.5px; }
  .portrait-frame { left: 628px; top: 474px; width: 187px; height: 154px; background: var(--white); border: 1px solid #dcdcdc; }
  .portrait { left: 633px; top: 478px; width: 177px; height: 145px;
    background: radial-gradient(ellipse at 55% 45%, #e9cf9a 0%, #c9a560 45%, #a08040 100%); }
  .read-more { left: 65px; top: 649px; width: 93px; height: 31px; background: var(--sky); color: var(--white); font-size: 11.5px; text-align: center; line-height: 31px; }

  .help { left: 0; top: 708px; width: 884px; height: 342px;
    background: linear-gradient(100deg, #0a0a08 0%, #0c0c0a 35%, #3a3933 55%, #5c5a50 72%, #2f2d28 88%, #1a1916 100%); }
  .help-title { left: 0; top: 738px; width: 884px; text-align: center; font-family: "Josefin Sans", sans-serif; font-weight: 300; font-size: 37px; color: var(--lime-soft); }
  .help-copy { left: 46px; top: 792px; width: 730px; text-align: center; font-family: "Roboto", sans-serif; font-size: 11px; line-height: 16px; color: var(--white); }
  .field { background: var(--white); font-family: "Roboto", sans-serif; font-size: 9px; color: #9a9a9a; padding: 9px 8px; }
  .send { left: 343px; top: 963px; width: 136px; height: 34px; background: var(--sky); color: var(--white); font-size: 12px; text-align: center; line-height: 34px; }

  .footer { left: 0; top: 1050px; width: 884px; height: 115px; background: var(--olive); }
  .foot-head { top: 1070px; font-size: 10.5px; color: #e6eec8; }
  .foot-link { font-family: "Roboto", sans-serif; font-size: 8.5px; color: var(--white); line-height: 16px; top: 1093px; }
  .news-input { left: 444px; top: 1094px; width: 152px; height: 22px; background: var(--white); font-family: "Roboto", sans-serif; font-size: 8.5px; color: #aaa; padding: 6px 7px; }
  .news-submit { left: 596px; top: 1094px; width: 54px; height: 22px; background: var(--submit); font-family: "Roboto", sans-serif; font-size: 9px; color: #2a2a2a; text-align: center; line-height: 22px; }
  .foot-social { top: 1090px; width: 26px; height: 26px; border-radius: 50%; }
  .copybar { left: 0; top: 1165px; width: 884px; height: 35px; background: var(--olive-dark); text-align: center; font-family: "Roboto", sans-serif; font-size: 8.5px; font-weight: 500; color: var(--white); line-height: 35px; }
  .copybar .link { color: var(--olive-link); font-weight: 400; }
</style>
</head>
<body>
<div class="canvas">
  <div class="abs topbar"></div>
  <div class="abs top-social one" role="img" aria-label="Social profile link"></div>
  <div class="abs top-social two" role="img" aria-label="Social profile link"></div>

  <div class="abs hero" role="img" aria-label="Calm photograph of smooth stones by misty blue water"></div>
  <div class="abs hero-shade"></div>

  <svg class="abs logo-disc" viewBox="0 0 240 162" aria-hidden="true">
    <path d="M5 92 A135 135 0 0 0 235 92" fill="none" stroke="rgba(0,0,0,0.25)" stroke-width="4" transform="translate(0 2)"/>
    <path d="M0 0 H240 V91 H236 A135 135 0 0 1 4 91 H0 Z" fill="#f5f5f5"/>
  </svg>
  <div class="abs brand-dot"></div>
  <div class="abs brand">
    <div class="brand-name">STILLBROOK</div>
    <div class="brand-sub">COUNSELING</div>
  </div>

  <div class="abs hero-name">Colette Brannigan</div>
  <div class="abs hero-title">LCSW, REGISTERED PLAY THERAPIST</div>

  <div class="abs nav"></div>
  <div class="abs nav-item" style="left:145px">Home</div>
  <div class="abs nav-item" style="left:233px">About Me</div>
  <div class="abs nav-item" style="left:342px">Counseling Services</div>
  <div class="abs nav-item" style="left:506px">Fees</div>
  <div class="abs nav-item" style="left:584px">FAQs</div>
  <div class="abs nav-item" style="left:667px">Contact Me</div>

  <h1 class="abs welcome-title">Colette Brannigan Welcomes You</h1>
  <div class="abs welcome-rule"></div>
  <div class="abs welcome-copy">
    <p>Duis gravida rhoncus enim vitae porttitor. Vivamus eget massa venenatis, aliquet mi vel, pellentesque ligula. Fusce sed massa sed orci condimentum efficitur in sit amet orci. Duis condimentum dolor eu sapien tempus dignissim. Nam elementum urna et erat luctus aliquam. Phasellus ut fringilla arcu, et dignissim lacus. Nulla facilisi. Mauris id nisi purus.</p>
    <p>Morbi ultrices tincidunt mauris in cursus. Phasellus vitae posuere justo. Nulla interdum elit quis nulla bibendum, at vulputate magna faucibus. Mauris tristique, nisi nec rutrum aliquet, nisl urna dignissim orci, ut cursus urna neque eu dolor.</p>
    <p>Aliquam quis elit risus. Donec finibus nisl sit amet finibus pulvinar. Nulla dignissim, neque ac tincidunt imperdiet, leo libero pellentesque leo, quis porta augue purus eget nunc. Cras vitae massa massa. Donec ultrices, turpis sit amet blandit ultrices, lectus metus lobortis mi, eget sodales lorem massa finibus dolor.</p>
  </div>
  <div class="abs portrait-frame"></div>
  <div class="abs portrait" role="img" aria-label="Portrait photograph of the therapist"></div>
  <div class="abs read-more">Read More</div>

  <div class="abs help" role="img" aria-label="Dark photograph of wet river rocks"></div>
  <h2 class="abs help-title">I’m Here To Help You.</h2>
  <p class="abs help-copy">If you have any&nbsp; queries on online presence and online store management and other web related things please send us mail with a brief of your question.</p>
  <div class="abs field" style="left:141px;top:864px;width:259px;height:28px">Your Name</div>
  <div class="abs field" style="left:141px;top:904px;width:259px;height:28px">Your Email id</div>
  <div class="abs field" style="left:423px;top:864px;width:260px;height:67px;padding-top:7px">Your Queries</div>
  <div class="abs send">Send</div>

  <div class="abs footer"></div>
  <div class="abs foot-head" style="left:55px">About</div>
  <div class="abs foot-head" style="left:146px">Counselling Services</div>
  <div class="abs foot-head" style="left:293px">Latest Posts</div>
  <div class="abs foot-head" style="left:440px">Subscribe Newsletter</div>
  <div class="abs foot-head" style="left:700px">Follow Me</div>
  <div class="abs foot-link" style="left:55px">Who I Am<br>Specialties<br>Approach</div>
  <div class="abs foot-link" style="left:146px">Individual Counseling<br>Play Therapy<br>Sandplay Therap</div>
  <div class="abs foot-link" style="left:293px">Lorem ipsumm dolor sit<br>Nuno valencia esdt di<br>Di maria nuno estelem</div>
  <div class="abs news-input">Your Email id</div>
  <div class="abs news-submit">Submit</div>
  <div class="abs foot-social" style="left:698px;background:var(--social-blue)" role="img" aria-label="Social profile link"></div>
  <div class="abs foot-social" style="left:733px;background:var(--social-sky)" role="img" aria-label="Social profile link"></div>
  <div class="abs foot-social" style="left:769px;background:var(--social-red)" role="img" aria-label="Social profile link"></div>

  <div class="abs copybar">Colette Brannigan© 2016 Copyright&nbsp; |&nbsp; <span class="link">Make an enquiry</span>&nbsp; |&nbsp; <span class="link">Privacy statement.</span></div>
</div>
</body>
</html>
```